verdant terraces simple classy business card design

my name is owen harlow and I run a gardening business aimed at high class verdant terraces. the business name is verdant terraces and our logo was designed on pixel forum .My clientel are anything from residential homes to businesses. I take pride in my work and know that I offer a service like no other in my area.
The business card will be used to represent my business and I want it to be not only rememberable, but simplistic and modern. Eye catching too. Of course I would like it relatable to gardening and appealing to the correct clientel - those being garden enthusiasts, prestigious homes and businesses that are after top of the line gardening services like no other on the market.
I am not a typical lawn mowing business so I don't want a typical card design that represents that. The gardens I work with are generally million dollar properties with owners who are very garden proud looking for upkeep and guidance from me along with sometimes whole new garden designs. I want the business cards to show to my clients that I take pride, as they do, in their garden. And I want them to know from my card that I am a professional, qualified horticulturist offering them a top of the line service for life. I want them to refer my business on. I want them to look at my business card and see class and professionalism in a modern unique bold way.
The card should be simple with the possibility of the logo on the front being embossed/debossed and my details on the back the card should have a organic garden feel it's very important to me that it is absolutely perfect
I am also very open to ideas and suggestions so look forward to seeing the designs. the business logo has been supplied with this project and I want the card to be double sided

Contact info is
Owen Harlow - Managing Director / Horticulturist
Phone : 0481 526 704
Email: owenharlow@verdantterraces.com.au

Target Market(s)

high class gardens residential and commercial

Industry/Entity Type

Gardener

Contact Information for Business Card

Contact info is
Phone : 0481 526 704

PLEASE MAKE CARD DOUBLE SIDED

Requirements
Must have
• organic simple classy modern feel
• must flow with the current logo that has been supplied with this project
• Double sided
• Must explain in a simple way that I deal with high end gardens and I'm a qualified horticulturist
Nice to have
• embossed debossed logo
Should not have
• shouldn't be to busy or cheap looking

```html
<!DOCTYPE html>
<html lang="en">
<head>
<meta charset="utf-8">
<title>Verdant Terraces – Business Card</title>
<link href="https://fonts.googleapis.com/css2?family=Roboto:wght@400;500&display=swap" rel="stylesheet">
<style>
  :root {
    --backdrop: #d9d9d6;
    --card: #1e1e1e;
    --card-sheen: #2a2a2a;
    --leaf: #5c9e50;
    --leaf-soft: #4a8541;
    --ink: #e6e6e6;
  }
  * { margin: 0; padding: 0; box-sizing: border-box; }
  html, body { width: 1200px; height: 1000px; overflow: hidden; }
  body {
    background: var(--backdrop);
    font-family: "Roboto", Arial, sans-serif;
    position: relative;
  }
  .card {
    position: absolute;
    left: 220px;
    width: 760px;
    background: linear-gradient(125deg, var(--card) 0%, var(--card) 55%, var(--card-sheen) 75%, var(--card) 100%);
    overflow: hidden;
  }
  .card--front { top: 50px; height: 432px; }
  .card--back { top: 523px; height: 437px; }

  .brand { display: flex; flex-direction: column; align-items: center; color: var(--leaf); font-weight: 400; text-transform: uppercase; }
  .brand__mark { width: 130px; height: 130px; border-radius: 50%; background: var(--leaf); }
  .brand__name { font-size: 58px; letter-spacing: 3px; line-height: 1; margin-top: 22px; }
  .brand__sub { font-size: 34px; letter-spacing: 30px; margin-right: -30px; margin-top: 10px; line-height: 1; }

  .card--front .brand { position: absolute; left: 0; right: 0; top: 60px; }

  .card--back .brand { position: absolute; right: 42px; top: 44px; }
  .card--back .brand__mark { width: 74px; height: 74px; }
  .card--back .brand__name { font-size: 30px; letter-spacing: 2px; margin-top: 12px; }
  .card--back .brand__sub { font-size: 17px; letter-spacing: 16px; margin-right: -16px; margin-top: 5px; }

  .motif {
    position: absolute; left: 0; top: 0; width: 230px; height: 100%;
    background: radial-gradient(ellipse at 30% 45%, var(--leaf) 0%, var(--leaf-soft) 55%, rgba(74,133,65,0) 100%);
  }
  .edge-tab { position: absolute; right: 0; top: 260px; width: 10px; height: 40px; background: var(--leaf); border-radius: 5px 0 0 5px; }

  .contact { position: absolute; right: 45px; top: 254px; text-align: right; color: var(--ink); }
  .contact__name { color: var(--leaf); font-size: 20px; font-weight: 500; }
  .contact__role { font-size: 16px; margin-top: 6px; letter-spacing: .3px; }
  .contact__list { list-style: none; margin-top: 22px; font-size: 16px; line-height: 23px; }
  .contact__list li { display: flex; justify-content: flex-end; align-items: center; gap: 8px; }
  .contact__list svg { width: 13px; height: 13px; fill: none; stroke: var(--leaf); stroke-width: 1.6; }
</style>
</head>
<body>
  <section class="card card--front" aria-label="Card front">
    <div class="brand">
      <span class="brand__mark" aria-hidden="true"></span>
      <span class="brand__name">Verdant</span>
      <span class="brand__sub">Terraces</span>
    </div>
  </section>

  <section class="card card--back" aria-label="Card back">
    <div class="motif" role="img" aria-label="Large decorative leafy tree motif in green"></div>
    <div class="brand">
      <span class="brand__mark" aria-hidden="true"></span>
      <span class="brand__name">Verdant</span>
      <span class="brand__sub">Terraces</span>
    </div>
    <span class="edge-tab" aria-hidden="true"></span>
    <div class="contact">
      <p class="contact__name">Owen Harlow</p>
      <p class="contact__role">Managing Director / Horticulturist</p>
      <ul class="contact__list">
        <li>0481 526 704
          <svg viewBox="0 0 13 13" aria-hidden="true"><rect x="3" y="0.8" width="7" height="11.4" rx="1.2"/><line x1="5.5" y1="10.2" x2="7.5" y2="10.2"/></svg>
        </li>
        <li>owenharlow@verdantterraces.com.au
          <svg viewBox="0 0 13 13" aria-hidden="true"><rect x="0.8" y="2.5" width="11.4" height="8" /><polyline points="0.8,2.5 6.5,7 12.2,2.5"/></svg>
        </li>
        <li>www.verdantterraces.com.au
          <svg viewBox="0 0 13 13" aria-hidden="true"><circle cx="6.5" cy="6.5" r="5.6"/><ellipse cx="6.5" cy="6.5" rx="2.4" ry="5.6"/><line x1="0.9" y1="6.5" x2="12.1" y2="6.5"/></svg>
        </li>
      </ul>
    </div>
  </section>
</body>
</html>
```